Design for signage on vans

I have purchased two new Valtroc Ferrin vans and i would like them designed so that there is brand synergy with our website etc.

our website is www.brelwick.ie

```html
<!DOCTYPE html>
<html lang="en">
<head>
<meta charset="utf-8">
<title>Brelwick IT Solutions – Van Livery</title>
<link rel="stylesheet" href="https://fonts.googleapis.com/css2?family=Arimo:wght@400&family=Michroma&display=swap">
<style>
  :root {
    --navy: #1f3452;
    --navy-light: #2a4265;
    --navy-dark: #182a43;
    --white: #ffffff;
    --red: #d2302c;
    --page: #ffffff;
  }
  * { margin: 0; padding: 0; box-sizing: border-box; }
  html, body { width: 1200px; height: 1200px; overflow: hidden; background: var(--page); }
  .canvas { position: relative; width: 1200px; height: 1200px; }

  .panel {
    position: absolute;
    background: linear-gradient(160deg, var(--navy-light) 0%, var(--navy) 45%, var(--navy-dark) 100%);
    color: var(--white);
    overflow: hidden;
  }
  .panel--side { left: 50px; top: 70px; width: 1100px; height: 420px; border-radius: 40px 70px 28px 28px; }
  .panel--rear { left: 328px; top: 600px; width: 545px; height: 420px; border-radius: 60px 60px 24px 24px; }

  .brand { position: absolute; }
  .brand__mark { position: absolute; left: 0; top: 0; }
  .brand__name, .brand__tagline {
    position: absolute; font-family: "Arimo", Arial, sans-serif; font-weight: 400; white-space: nowrap; line-height: 1;
  }
  .brand__rule { position: absolute; height: 2px; background: var(--red); }

  .panel--side .brand { left: 44px; top: 70px; }
  .panel--side .brand__name { left: 140px; top: 0; font-size: 64px; letter-spacing: -1px; }
  .panel--side .brand__rule { left: 140px; top: 74px; width: 282px; }
  .panel--side .brand__tagline { left: 140px; top: 82px; font-size: 52px; letter-spacing: -0.5px; }

  .panel--rear .brand { left: 85px; top: 50px; }
  .panel--rear .brand__name { left: 112px; top: 0; font-size: 46px; letter-spacing: -1px; }
  .panel--rear .brand__rule { left: 112px; top: 54px; width: 230px; }
  .panel--rear .brand__tagline { left: 112px; top: 60px; font-size: 40px; letter-spacing: -0.5px; }

  .contact { position: absolute; font-family: "Michroma", "Arial Black", sans-serif; white-space: nowrap; line-height: 1; }
  .panel--side .contact--web { left: 532px; top: 250px; font-size: 17px; letter-spacing: 2px; }
  .panel--side .contact--phone { left: 532px; top: 276px; font-size: 19px; letter-spacing: 2px; }
  .panel--rear .contact--web { left: 0; right: 0; text-align: center; top: 192px; font-size: 19px; letter-spacing: 2px; }
  .panel--rear .contact--phone { left: 0; right: 0; text-align: center; top: 254px; font-size: 26px; letter-spacing: 3px; }

  .stripe { position: absolute; left: 50px; right: 50px; top: 294px; height: 8px; background: var(--red); }
</style>
</head>
<body>
<main class="canvas">
  <section class="panel panel--side" role="img" aria-label="Side van panel in navy with faint circuit-board line pattern">
    <div class="brand">
      <svg class="brand__mark" width="120" height="120" viewBox="0 0 120 120" aria-hidden="true">
        <circle cx="58" cy="58" r="52" fill="none" stroke="var(--white)" stroke-width="4"/>
      </svg>
      <span class="brand__name">Brelwick</span>
      <span class="brand__rule"></span>
      <span class="brand__tagline">IT Solutions</span>
    </div>
    <p class="contact contact--web">www.brelwick.ie</p>
    <p class="contact contact--phone">234-555-0172</p>
  </section>

  <section class="panel panel--rear" role="img" aria-label="Rear van doors in navy with faint circuit-board line pattern">
    <div class="brand">
      <svg class="brand__mark" width="95" height="95" viewBox="0 0 95 95" aria-hidden="true">
        <circle cx="46" cy="46" r="42" fill="none" stroke="var(--white)" stroke-width="3.5"/>
      </svg>
      <span class="brand__name">Brelwick</span>
      <span class="brand__rule"></span>
      <span class="brand__tagline">IT Solutions</span>
    </div>
    <p class="contact contact--web">www.brelwick.ie</p>
    <p class="contact contact--phone">234-555-0172</p>
    <span class="stripe"></span>
  </section>
</main>
</body>
</html>
```